Etiketten-Design für Trinkweine
Zielgruppe
Wir sind eine Weinkellerei, die einfache Trinkweine für den LEH herstellt.
Unsere Zielgruppen sind Jugendliche .
Wir suchen ein Etikett für unser neues Produkt ,,Traubensaftschorle`` alkoholfrei
Aufgabenstellung
Siehe Anhang , eigene ideen sind auch erwünscht.
Das Etikett sollte Natur verbunden wirken da es ein Bio Produkt ist.
Farben: weiß, grün wären erwünscht.
Das Etikett sollte 75mm hoch und 120mm Breit sein
Strukturpapier weiß
Anbei auch unserer Standartetikett gerne kann das Logo übernommen werden

```html
<!DOCTYPE html>
<html lang="de">
<head>
<meta charset="utf-8">
<title>Traubensaftschorle – Etikett</title>
<link rel="stylesheet" href="https://fonts.googleapis.com/css2?family=Griffy&family=Delius&display=swap">
<style>
  :root {
    --canvas-bg: #eef1ec;
    --label-pattern: #dcefdf;
    --label-pattern-deep: #cbe6cf;
    --circle-line: #b7dcbc;
    --paper: #ffffff;
    --ink: #111111;
    --fold-line: #1a1a1a;
  }
  * { margin: 0; padding: 0; box-sizing: border-box; }
  html, body {
    width: 1200px; height: 1200px; overflow: hidden;
    background: var(--canvas-bg);
  }
  .canvas { position: relative; width: 1200px; height: 1200px; }
  .label {
    position: absolute; left: 60px; top: 262px;
    width: 1080px; height: 675px;
    display: flex;
    box-shadow: 0 6px 24px rgba(0,0,0,0.12);
  }
  .panel {
    position: relative; width: 540px; height: 675px;
  }
  .panel-pattern {
    position: absolute; inset: 0;
    background: radial-gradient(circle at 50% 50%, var(--label-pattern) 0%, var(--label-pattern-deep) 100%);
  }
  .fold-line {
    position: absolute; left: 539px; top: 0; width: 2px; height: 675px;
    background: repeating-linear-gradient(to bottom, var(--fold-line) 0 22px, transparent 22px 36px);
    z-index: 2;
  }
  .brand {
    position: absolute; left: 0; right: 0; top: 28px;
    text-align: center;
    font-family: "Delius", cursive;
    font-size: 30px; color: var(--ink);
  }
  .brand span { background: var(--paper); padding: 4px 12px; }
  .seal {
    position: absolute; left: 66px; top: 133px;
    width: 408px; height: 408px; border-radius: 50%;
    background: var(--paper);
    border: 3px solid var(--circle-line);
    display: flex; flex-direction: column; align-items: center; justify-content: center;
    text-align: center; color: var(--ink);
  }
  .product-name {
    font-family: "Griffy", cursive;
    font-size: 70px; line-height: 1.45;
    margin-top: 10px;
  }
  .volume {
    font-family: "Griffy", cursive;
    font-size: 24px; margin-top: 8px;
  }
  .back-info {
    font-family: "Delius", cursive;
    font-size: 23px; line-height: 1.5;
  }
  .back-info p + p { margin-top: 34px; }
</style>
</head>
<body>
<main class="canvas">
  <section class="label">
    <div class="panel front">
      <div class="panel-pattern" role="img" aria-label="Feines hellgrünes Linienornament mit Ranken, Blättern und Trauben"></div>
      <div class="brand"><span>Petra Finkel</span></div>
      <div class="seal">
        <h1 class="product-name">TRAUBEN<br>· SAFT ·<br>SCHORLE</h1>
        <p class="volume">0,33 L</p>
      </div>
    </div>
    <div class="fold-line"></div>
    <div class="panel back">
      <div class="panel-pattern" role="img" aria-label="Feines hellgrünes Linienornament mit Ranken, Blättern und Trauben"></div>
      <div class="seal back-info">
        <p>Trauben saft mit<br>zugestlew kohlensäure</p>
        <p>VOS Nr. 01/20</p>
        <p>Abfüller: Petra Finkel<br>Rebgasse 7c<br>79288 Sonnfeld</p>
      </div>
    </div>
  </section>
</main>
</body>
</html>
```